Brenwick Drilling Inc. Business card design

Business card design for "Brenwick Drilling Inc. - Directional Drilling Services"

Address is:

Brenwick Drilling Inc.
512 - 73 Tolvane Crescent SW
Calgary, Alberta, Canada
T2K 4P8

Please incorporate the logo design into the card, thank you.

Target Market(s)

Oil & Gas and Drilling

Industry/Entity Type

Business

```html
<!DOCTYPE html>
<html lang="en">
<head>
<meta charset="UTF-8">
<title>Brenwick Drilling Inc. – Business Card</title>
<link rel="stylesheet" href="https://fonts.googleapis.com/css2?family=Exo+2:wght@500;700&family=Mulish:wght@400;500&display=swap">
<style>
  :root {
    --bg: #ecebe8;
    --card: #ffffff;
    --ink: #1a1a1a;
    --red: #d7191c;
    --muted: #444444;
    --ghost: #ededed;
    --shadow: rgba(0,0,0,0.18);
  }
  * { box-sizing: border-box; margin: 0; padding: 0; }
  html, body { width: 1200px; height: 900px; overflow: hidden; }
  body {
    background: var(--bg);
    font-family: "Mulish", sans-serif;
    color: var(--ink);
    position: relative;
  }
  .card {
    position: absolute;
    left: 230px;
    width: 740px;
    height: 423px;
    background: var(--card);
    box-shadow: 0 6px 18px var(--shadow);
    overflow: hidden;
  }
  .card--front { top: 20px; }
  .card--back { top: 460px; }

  .ghost-ring {
    position: absolute;
    border-radius: 50%;
    background: var(--ghost);
  }
  .card--front .ghost-ring { width: 300px; height: 300px; left: -130px; top: 70px; }
  .card--back .ghost-ring { width: 280px; height: 280px; right: -70px; top: 40px; }

  .brand {
    position: absolute;
    display: flex;
    flex-direction: column;
    align-items: center;
  }
  .brand__mark {
    width: 54px; height: 54px;
    border-radius: 50%;
    border: 5px solid var(--red);
    margin-bottom: 12px;
  }
  .brand__name {
    font-family: "Exo 2", sans-serif;
    font-weight: 700;
    font-size: 26px;
    letter-spacing: 1px;
    color: var(--ink);
    line-height: 1;
  }
  .brand__tagline {
    font-family: "Exo 2", sans-serif;
    font-weight: 500;
    font-size: 11.5px;
    letter-spacing: 4.4px;
    color: var(--ink);
    margin-top: 4px;
  }
  .card--front .brand { left: 0; right: 0; top: 130px; }
  .card--back .brand { right: 40px; top: 190px; }
  .card--back .brand__name { font-size: 22px; }
  .card--back .brand__tagline { font-size: 10px; letter-spacing: 3.7px; }
  .card--back .brand__mark { width: 48px; height: 48px; }

  .person { position: absolute; left: 56px; top: 70px; }
  .person__name {
    font-family: "Exo 2", sans-serif;
    font-weight: 700;
    font-size: 24px;
    color: var(--red);
    letter-spacing: 0.5px;
  }
  .person__title { font-size: 17px; font-weight: 500; color: var(--ink); }

  .address {
    position: absolute;
    right: 48px; top: 34px;
    text-align: right;
    font-size: 15.5px;
    line-height: 1.3;
    color: var(--ink);
  }

  .contacts { position: absolute; left: 56px; bottom: 46px; list-style: none; }
  .contacts li {
    display: flex; align-items: center; gap: 16px;
    font-size: 19px; font-weight: 500; line-height: 1.6;
  }
  .contacts svg { width: 18px; height: 18px; fill: none; stroke: var(--red); stroke-width: 2; }
  .contacts .fill { fill: var(--red); stroke: none; }
</style>
</head>
<body>

<section class="card card--front" aria-label="Card front">
  <div class="ghost-ring"></div>
  <div class="brand">
    <div class="brand__mark"></div>
    <div class="brand__name">BRENWICK DRILLING INC.</div>
    <div class="brand__tagline">DIRECTIONAL DRILLING SERVICES</div>
  </div>
</section>

<section class="card card--back" aria-label="Card back">
  <div class="ghost-ring"></div>
  <address class="address" style="font-style:normal">
    Brenwick Drilling Inc.<br>
    512 - 73 Tolvane Crescent SW<br>
    Calgary, Alberta, Canada<br>
    T2K 4P8
  </address>

  <div class="person">
    <div class="person__name">MARK DELANEY</div>
    <div class="person__title">Director</div>
  </div>

  <ul class="contacts">
    <li>
      <svg viewBox="0 0 24 24"><path class="fill" d="M6.6 10.8a15.5 15.5 0 0 0 6.6 6.6l2.2-2.2c.3-.3.7-.4 1-.2 1.1.4 2.3.6 3.6.6.6 0 1 .4 1 1V20c0 .6-.4 1-1 1A17 17 0 0 1 3 4c0-.6.4-1 1-1h3.5c.6 0 1 .4 1 1 0 1.3.2 2.5.6 3.6.1.3 0 .7-.2 1z"/></svg>
      +123 555 0147
    </li>
    <li>
      <svg viewBox="0 0 24 24"><rect class="fill" x="2" y="5" width="20" height="14" rx="1"/><path d="M3 6l9 7 9-7" stroke="#fff"/></svg>
      mdelaney@brenwickmail.com
    </li>
    <li>
      <svg viewBox="0 0 24 24"><circle cx="12" cy="12" r="9"/><path d="M3 12h18M12 3c3 3 3 15 0 18M12 3c-3 3-3 15 0 18"/></svg>
      www.brenwickdrilling.com
    </li>
  </ul>

  <div class="brand">
    <div class="brand__mark"></div>
    <div class="brand__name">BRENWICK DRILLING INC.</div>
    <div class="brand__tagline">DIRECTIONAL DRILLING SERVICES</div>
  </div>
</section>

</body>
</html>
```